Web Design Project

Psychotherapy and Counselling Practice needs a landing page web design.

My business "Larkspur Advisory" specialises in the treatment of Anxiety and Depression with a holistic approach, endeavouring to unlock the key that holds us to ransom in a life that is imbalanced, frustrating, and ultimately of our own making due to our own perceptions and behaviours.

There is much that impacts us which we cannot change, but we are always in control of how we think, and how we frame our experiences.....learning to challenge those thoughts and behaviours that are destructive and disempowering opens up a world of joyful possibility. Life is about making choices, learn to make wiser and healthier choices.......

Larkspur Advisory has a client base of individual clients but will seek to expand to offer services to the Corporate world by offering an adjunct to employers for established "Wellness Programs".

Larkspur Advisory is a highly professional, ethically bound business, with the needs of the client at the forefront of all we do.

Larkspur Advisory wishes to avoid the usual "jargon driven" psychobabble offered on many counselling web pages. It aims to be stylishly presented, clean in look and with as few "words" as possible and a largely white background (faster loading and more powerful impact of what is stated), those words contained in the webpage should be meaningful, persuasive and have an impact simply at glance. Larkspur does not want , or expect, those prospective clients in need of support , to be reading through volumes of industry driven cliches.

At this point Larkspur is just looking for a high quality landing page. However in time this will likely expand to include other sections such as case studies, video content etc.

Target Market(s)

Those in need of emotional support, suffering mental health issues, and those simply wanting to become self aware supported by a mindful therapist.

Industry/Entity Type

Industry

Requirements
Must have
• The design must incorporate the Larkspur logo and colour schemes found on the attached files.

```html
<!DOCTYPE html>
<html lang="en">
<head>
<meta charset="utf-8">
<title>Larkspur Advisory</title>
<link href="https://fonts.googleapis.com/css2?family=PT+Sans:wght@400;700&family=Arimo:wght@700&display=swap" rel="stylesheet">
<style>
  :root {
    --green: #8fad10;
    --green-dark: #7fa300;
    --grey: #747474;
    --grey-dark: #5e5e5e;
    --grey-text: #9a9a9a;
    --body-text: #444;
    --hero-light: #fbfbfb;
    --white: #fff;
  }
  * { margin: 0; padding: 0; box-sizing: border-box; }
  html, body { width: 1200px; height: 1000px; overflow: hidden; background: var(--white); }
  body { position: relative; font-family: "PT Sans", sans-serif; }

  .main-nav {
    position: absolute; left: 85px; top: 144px; width: 614px; height: 44px;
    background: var(--green); border-radius: 4px;
  }
  .main-nav a {
    position: absolute; top: 12px; color: var(--white); text-decoration: none;
    font-weight: 700; font-size: 14.5px;
  }

  .practitioner { position: absolute; left: 786px; top: 94px; }
  .brand-tile {
    position: absolute; left: 0; top: 0; width: 95px; height: 94px;
    background: var(--grey); border-radius: 3px;
    display: flex; align-items: center; justify-content: center;
    color: var(--white); font-size: 15px; letter-spacing: 0.5px;
  }
  .practitioner-name {
    position: absolute; left: 106px; top: 22px; white-space: nowrap;
    color: var(--grey-text); font-size: 19px; letter-spacing: 0.5px;
  }
  .practitioner-credentials {
    position: absolute; left: 107px; top: 49px; white-space: nowrap;
    color: var(--grey-text); font-size: 14px;
  }

  .hero { position: absolute; left: 223px; top: 232px; width: 750px; height: 419px; }
  .hero-art {
    position: absolute; left: 0; top: 0; width: 750px; height: 419px;
    background: linear-gradient(to bottom, var(--hero-light) 0%, var(--hero-light) 80%, #b8c478 87%, var(--grey) 100%);
  }
  .hero-wordmark {
    position: absolute; left: 50px; top: 186px; color: var(--grey);
    font-size: 50px; letter-spacing: 3px;
  }
  .news { position: absolute; left: 338px; top: 18px; width: 405px; }
  .news h2 { color: var(--green); font-size: 19px; font-weight: 700; }
  .news p { margin-top: 14px; color: var(--body-text); font-size: 14px; line-height: 19px; }

  .tagline { position: absolute; left: 228px; top: 727px; display: flex; align-items: center; }
  .tagline-mark { width: 138px; height: 39px; background: var(--grey-dark); border-radius: 3px; }
  .tagline-text { margin-left: 6px; font-size: 14px; color: var(--grey-dark); letter-spacing: 0.3px; }

  .contact { position: absolute; left: 712px; top: 708px; color: var(--grey-text); font-size: 14px; }
  .contact p { line-height: 21px; }
  .contact .site { color: var(--grey-dark); margin-bottom: 6px; }
  .contact .site strong { color: var(--green); font-size: 18px; font-weight: 400; }

  .site-footer {
    position: absolute; left: 46px; top: 795px; width: 1104px; height: 54px;
    background: var(--green-dark); border-radius: 2px;
  }
  .copyright {
    position: absolute; left: 179px; top: 23px; color: var(--white);
    font-family: "Arimo", sans-serif; font-weight: 700; font-size: 8.5px;
  }
  .social { position: absolute; top: 11px; width: 32px; height: 31px; background: var(--white); border-radius: 6px; }
</style>
</head>
<body>
  <nav class="main-nav">
    <a href="#" style="left:288px">Home</a>
    <a href="#" style="left:356px">About Us</a>
    <a href="#" style="left:445px">Contact</a>
    <a href="#" style="left:524px">Our services</a>
  </nav>

  <div class="practitioner">
    <div class="brand-tile">Larkspur</div>
    <div class="practitioner-name">MARA HOLT</div>
    <div class="practitioner-credentials">BA (Psych) BSc (Hons) Psych MBPS</div>
  </div>

  <section class="hero">
    <div class="hero-art" role="img" aria-label="Hero illustration: climbing vine above a green and grey landscape band"></div>
    <div class="hero-wordmark">Larkspur</div>
    <div class="news">
      <h2>What’s News</h2>
      <p>Nulla vitae elit libero, a pharetra augue. Maecenas faucibus mollis interdum. Donec id elit non mi porta gravida at eget metus. Morbi leo risus, porta ac consectetur ac, vestibulum at eros. Sed posuere consectetur est at lobortis. Praesent commodo cursus magna, vel scelerisque nisl consectetur et.</p>
    </div>
  </section>

  <div class="tagline">
    <div class="tagline-mark"></div>
    <span class="tagline-text">Larkspur Advisory is highly Professional</span>
  </div>

  <div class="contact">
    <p class="site">www.<strong>larkspuradvisory</strong>.com.au</p>
    <p>Mobile: 0412 555 018</p>
    <p>E-mail: mara.holt@larkspurmail.com</p>
  </div>

  <footer class="site-footer">
    <span class="copyright">(C) Copyright 2013 - Larkspur - All rights reserved</span>
    <span class="social" style="left:843px" role="img" aria-label="Social profile link"></span>
    <span class="social" style="left:883px" role="img" aria-label="Social profile link"></span>
  </footer>
</body>
</html>
```